Bref créative
Vorlinsa Granola Label
Front & Back Package Label
We are a new, small granola company looking for a front and back label for our retail package.
Food
Retail Market
We would like an eye catching label based on our current logo.
Logo file
front text only (not layout) for design
back text only (not layout) for design
Bag the product will be packed in.

```html
<!DOCTYPE html>
<html lang="en">
<head>
<meta charset="utf-8">
<title>Vorlinsa Granola – Front &amp; Back Label</title>
<link href="https://fonts.googleapis.com/css2?family=Oswald:wght@500;700&family=Open+Sans:wght@400;700&family=Kaushan+Script&display=swap" rel="stylesheet">
<style>
  :root {
    --cream: #f4ecd8;
    --brown: #5b3a1f;
    --brown-dark: #43290f;
    --green: #8dc63f;
    --green-dark: #5f9a2a;
    --ink: #2d2414;
    --page: #ffffff;
  }
  * { box-sizing: border-box; margin: 0; padding: 0; }
  html, body { width: 1200px; height: 778px; overflow: hidden; background: var(--page); }
  .canvas { position: relative; width: 1200px; height: 778px; }

  .label {
    position: absolute; top: 120px; width: 535px; height: 540px;
    background: var(--cream); border-radius: 30px; overflow: hidden;
    box-shadow: 0 2px 6px rgba(0,0,0,.12);
  }
  .label--front { left: 50px; }
  .label--back { left: 615px; }

  .label__bands { position: absolute; left: 0; top: 0; width: 535px; height: 540px; }

  .ribbon {
    position: absolute; display: flex; align-items: center; justify-content: center;
    font-family: "Oswald", sans-serif; font-weight: 700; white-space: nowrap;
  }
  .ribbon--gluten { left: -70px; top: 42px; width: 340px; height: 40px; background: var(--brown); color: var(--cream); font-size: 19px; transform: rotate(-33deg); }
  .ribbon--blend { left: -50px; top: 92px; width: 380px; height: 44px; background: var(--green); color: var(--brown-dark); font-size: 21px; transform: rotate(-33deg); }
  .ribbon--decadent {
    right: -20px; top: 52px; width: 300px; height: 52px; background: var(--brown); color: var(--cream);
    font-family: "Kaushan Script", cursive; font-weight: 400; font-size: 26px; transform: rotate(-22deg);
  }

  .brand {
    position: absolute; display: flex; align-items: center; gap: 12px;
    font-family: "Oswald", sans-serif; font-weight: 700; color: var(--green-dark);
    line-height: .95; text-transform: uppercase; white-space: nowrap;
  }
  .brand__mark { background: var(--green-dark); flex: none; }
  .brand--front { left: 160px; top: 160px; font-size: 58px; }
  .brand--front .brand__mark { width: 24px; height: 24px; }
  .brand--back { left: 32px; top: 30px; font-size: 34px; }
  .brand--back .brand__mark { width: 16px; height: 16px; }

  .tag-fruits {
    position: absolute; background: var(--cream); color: var(--brown-dark);
    font-family: "Oswald", sans-serif; font-weight: 700; white-space: nowrap;
    padding: 4px 10px; line-height: 1;
  }
  .tag-fruits__big { color: var(--green-dark); font-size: 1.45em; }
  .tag-fruits--front { left: 20px; top: 358px; font-size: 22px; }
  .tag-fruits--back { right: 16px; top: 462px; font-size: 17px; }

  .tagline {
    position: absolute; left: 200px; top: 410px; white-space: nowrap;
    font-family: "Kaushan Script", cursive; font-size: 40px; line-height: 1.2; color: var(--cream);
    transform: rotate(-6deg);
  }
  .net-weight {
    position: absolute; right: 26px; bottom: 22px; white-space: nowrap;
    font-family: "Open Sans", sans-serif; font-weight: 700; font-size: 12px; color: var(--cream);
  }

  .copy {
    position: absolute; left: 28px; width: 480px;
    font-family: "Open Sans", sans-serif; font-size: 10px; line-height: 1.4; color: var(--ink);
  }
  .copy p + p { margin-top: 9px; }
  .copy strong { font-weight: 700; }
  .copy--story { top: 168px; }
  .copy--story .copy__lead { color: #fff; }
  .copy--details { top: 330px; }
  .company { margin-top: 10px; }
</style>
</head>
<body>
<main class="canvas">

  <section class="label label--front" aria-label="Front label">
    <svg class="label__bands" viewBox="0 0 535 540" aria-hidden="true">
      <polygon fill="var(--brown)" points="0,340 40,334 70,342 110,330 150,338 200,326 250,334 300,322 350,330 400,318 450,326 500,314 535,320 535,540 0,540"/>
      <polygon fill="var(--green)" points="0,352 60,340 120,332 180,322 240,314 300,304 360,296 420,286 480,278 535,270 535,352 500,360 460,356 420,366 380,362 340,372 300,368 260,380 220,376 180,388 140,384 100,396 60,392 20,402 0,400"/>
    </svg>
    <div class="ribbon ribbon--gluten">Naturally Gluten Free</div>
    <div class="ribbon ribbon--blend">Chef's Original Blend</div>
    <div class="brand brand--front"><span class="brand__mark"></span><span>Vorlinsa<br>Granola</span></div>
    <div class="tag-fruits tag-fruits--front">with <span class="tag-fruits__big">Fruits &amp; Nuts !</span></div>
    <div class="tagline">Simply Decadent!</div>
    <div class="net-weight">Net Weight 12 Ounces</div>
  </section>

  <section class="label label--back" aria-label="Back label">
    <svg class="label__bands" viewBox="0 0 535 540" aria-hidden="true">
      <polygon fill="var(--green)" points="0,150 50,144 100,152 150,140 200,148 250,136 300,146 350,134 400,142 450,130 500,138 535,132 535,310 490,318 440,308 390,320 340,312 290,324 240,314 190,326 140,316 90,328 40,318 0,326"/>
      <polygon fill="var(--brown)" points="0,470 50,462 100,470 150,458 200,466 250,454 300,462 350,450 400,458 450,446 500,454 535,448 535,540 0,540"/>
      <polygon fill="var(--green)" points="0,494 80,484 160,476 240,466 320,458 400,448 535,436 535,468 470,478 400,476 320,488 240,492 160,502 80,506 0,516"/>
    </svg>
    <div class="ribbon ribbon--decadent">Simply Decadent!</div>
    <div class="brand brand--back"><span class="brand__mark"></span><span>Vorlinsa<br>Granola</span></div>

    <div class="copy copy--story">
      <p><strong class="copy__lead">Why is Vorlinsa Granola simply decadent?</strong> Because it's made with the best ingredients and artfully baked in small batches. It is just sweet enough without being high in sugar and it is gluten free without using ingredients that are difficult to pronounce. This is food that your great grandmother would recognize as food! It's not made in a flavor factory, nothing artificial, no chemical preservatives. It's made by a chef who understands that eating well does not mean you have to sacrifice flavor or enjoyment.</p>
      <p>Vorlinsa Granola will make you look forward to eating breakfast everyday. In fact it is so delicious you may find yourself eating it for lunch and dinner too! Go ahead, we won't judge.</p>
    </div>

    <div class="copy copy--details">
      <p><strong>Ingredients:</strong><br>Certified Gluten Free Oats, Organic Unsweetened Coconut, Organic Dried Apples, Organic Dried Cranberries, Organic Almonds, Organic Flaxseed Meal, Honey, Organic Brown Sugar, Extra Virgin Coconut Oil, Organic Rice Flour, Crystallized Ginger, Vanilla, Spices.</p>
      <p><strong>Allergen Information: Contains Nuts</strong></p>
      <p class="company"><strong>Vorlinsa Granola Company</strong><br>Elm Harbor, NY<br>info@vorlinsa.com</p>
    </div>

    <div class="tag-fruits tag-fruits--back">with <span class="tag-fruits__big">Fruits &amp; Nuts !</span></div>
  </section>

</main>
</body>
</html>
```